Tribe as pace "La tribu marca el paso"

I'm writing a book about word of mouth and the consumer as the media "the book is in Spanish" so you have to use "La tribu marca el paso" the subtitle is and 30 examples that proves it "Más 30 relatos de la plaza"

Book is about the power of consumer nowadays , the book will combine the era of social media but also the power of one to one word of mouth meaning w/o being connected to an electronic platform

Tribe sets the pace is a book about the power that now the consumer has in this double way interaction between the brands and the consumer, between the services and the people between the social media and the traditional media.

Consumer is on control and it is because "tribe sets the pace"

About book principles
I love simple books white background, simplicity around the fonts and the images (simple is better)

Target Market(s)

Marketing and digital marketing managers, social media managers, community managers, social media agencies, business people

Industry/Entity Type

Electronic

Requirements
Must have
• White backgroung, black and red fonts big fonts
Nice to have
• the subtitle "Más 30 relatos de la calle"

```html
<!DOCTYPE html>
<html lang="es">
<head>
<meta charset="utf-8">
<title>La tribu marca el paso — cubierta</title>
<link rel="stylesheet" href="https://fonts.googleapis.com/css2?family=Jost:wght@400;500;600;700&display=swap">
<style>
  :root {
    --stage: #ececec;
    --paper: #ffffff;
    --ink: #111111;
    --accent: #d81e2a;
    --ghost: #e8e8e8;
    --box: #1a1a1a;
    --box-label: #9a9a9a;
    --edge: #d6d6d6;
  }
  * { margin: 0; padding: 0; box-sizing: border-box; }
  html, body { width: 1200px; height: 800px; overflow: hidden; }
  body {
    background: var(--stage);
    font-family: "Jost", "Futura", sans-serif;
    color: var(--ink);
    position: relative;
  }
  .jacket {
    position: absolute;
    left: 156px; top: 100px;
    display: flex;
    height: 600px;
    box-shadow: 0 14px 40px rgba(0,0,0,.12);
  }
  .back-cover, .spine, .front-cover {
    background: var(--paper);
    position: relative;
    height: 100%;
    overflow: hidden;
  }
  .back-cover { width: 420px; padding: 26px 30px; border-right: 1px solid var(--edge); }
  .spine { width: 48px; border-right: 1px solid var(--edge); }
  .front-cover { width: 420px; }

  /* back cover */
  .back-author {
    text-align: right; font-weight: 700; font-size: 12px;
    letter-spacing: .04em; text-transform: uppercase;
  }
  .back-title { text-transform: uppercase; font-weight: 500; line-height: .92; margin-top: 6px; }
  .back-title .line-one { display: block; font-size: 38px; }
  .back-title .line-two { display: block; font-size: 64px; }
  .back-subtitle {
    color: var(--accent); font-weight: 600; font-size: 19px;
    text-transform: uppercase; margin-top: 10px; letter-spacing: .01em;
  }
  .back-blurb {
    margin-top: 22px; font-size: 10.4px; line-height: 1.42;
    font-weight: 600; text-align: justify; text-align-last: center;
  }
  .back-marks {
    position: absolute; left: 30px; right: 30px; bottom: 30px;
    display: flex; justify-content: space-between;
  }
  .mark-box {
    width: 112px; height: 50px; background: var(--box);
    color: var(--box-label); font-size: 11px;
    display: flex; align-items: center; justify-content: center;
    letter-spacing: .05em;
  }

  /* spine */
  .spine-text {
    position: absolute; left: 0; right: 0; top: 24px; bottom: 24px;
    writing-mode: vertical-rl;
    display: flex; justify-content: space-between; align-items: center;
    text-transform: uppercase;
  }
  .spine-title { font-size: 25px; font-weight: 500; letter-spacing: .02em; }
  .spine-author { font-size: 10px; font-weight: 700; letter-spacing: .06em; }

  /* front cover */
  .ghost-word {
    position: absolute; color: var(--ghost); font-weight: 500;
    text-transform: uppercase; line-height: 1;
  }
  .ghost-word.upper { left: 150px; top: 172px; font-size: 92px; }
  .ghost-word.lower { left: 86px; top: 470px; font-size: 100px; }
  .ghost-word.column {
    right: 28px; top: 26px; font-size: 34px; width: 40px;
    text-align: center; line-height: 40px;
  }
  .ghost-word.column.left { left: 82px; right: auto; top: 70px; }
  .rise-arrow { position: absolute; left: 34px; top: 18px; }
  .title-block { position: absolute; inset: 0; text-transform: uppercase; font-weight: 500; }
  .title-lead { position: absolute; left: 126px; top: 34px; font-size: 44px; line-height: 44px; }
  .title-column {
    position: absolute; left: 130px; top: 80px; width: 44px;
    font-size: 42px; line-height: 40px; text-align: center;
  }
  .title-column span { display: block; height: 40px; }
  .title-cross-left, .title-cross-right {
    position: absolute; top: 320px; font-size: 46px; line-height: 40px;
  }
  .title-cross-left { right: 290px; }
  .title-cross-left .small { font-size: 34px; margin-right: 4px; }
  .title-cross-right { left: 176px; }
  .front-subtitle {
    position: absolute; left: 184px; top: 392px;
    color: var(--accent); font-weight: 600; font-size: 21px;
    line-height: 1.25; text-transform: uppercase;
  }
  .front-author {
    position: absolute; right: 30px; bottom: 30px;
    font-weight: 700; font-size: 14px; letter-spacing: .04em; text-transform: uppercase;
  }
</style>
</head>
<body>
  <main class="jacket">
    <section class="back-cover">
      <p class="back-author">Tomás Echeverri</p>
      <h2 class="back-title"><span class="line-one">La tribu marca</span><span class="line-two">el paso</span></h2>
      <p class="back-subtitle">Más 30 relatos de la plaza</p>
      <p class="back-blurb">Lorem ipsum dolor sit amet, consectetur adipisicing elit, sed do eiusmod tempor incididunt ut labore et dolore magna aliqua. Ut enim ad minim veniam, quis nostrud exercitation. Lorem ipsum dolor sit amet, consectetur adipisicing elit, sed do eiusmod tempor incididunt ut labore et dolore magna aliqua. Ut enim ad minim veniam, quis nostrud exercitation. Lorem ipsum dolor sit amet, consectetur adipisicing elit, sed do eiusmod tempor incididunt ut labore et dolore magna aliqua. Ut enim ad minim veniam, quis nostrud exercitation. Lorem ipsum dolor sit amet, consectetur adipisicing elit, sed do eiusmod tempor incididunt ut labore et dolore magna aliqua. Ut enim ad minim veniam, quis nostrud exercitation. Lorem ipsum dolor sit amet, consectetur adipisicing elit, sed do eiusmod tempor incididunt ut labore et dolore magna aliqua. Ut enim ad minim veniam, quis nostrud exercitation. Lorem ipsum dolor sit amet, consectetur adipisicing elit, sed do eiusmod tempor incididunt ut labore et dolore magna aliqua. Ut enim ad minim veniam, quis nostrud exercitation.</p>
      <div class="back-marks">
        <div class="mark-box">LOGO</div>
        <div class="mark-box">ISBN</div>
      </div>
    </section>

    <section class="spine">
      <div class="spine-text">
        <span class="spine-title">La tribu marca el paso</span>
        <span class="spine-author">Tomás Echeverri</span>
      </div>
    </section>

    <section class="front-cover">
      <div class="ghost-word column left" aria-hidden="true">T<br>R<br>I<br>B<br>U</div>
      <div class="ghost-word upper" aria-hidden="true">Paso</div>
      <div class="ghost-word lower" aria-hidden="true">Paso</div>
      <div class="ghost-word column" aria-hidden="true">M<br>A<br>R<br>C<br>A<br>E<br>L<br>P<br>A<br>S<br>O</div>

      <svg class="rise-arrow" width="40" height="566" viewBox="0 0 40 566" aria-hidden="true">
        <rect x="14" y="36" width="12" height="530" fill="var(--accent)"/>
        <polygon points="20,0 40,40 0,40" fill="var(--accent)"/>
      </svg>

      <h1 class="title-block">
        <span class="title-lead">La</span>
        <span class="title-column"><span>T</span><span>R</span><span>I</span><span>B</span><span>U</span><span>M</span><span>A</span><span>R</span><span>C</span><span>A</span></span>
        <span class="title-cross-left"><span class="small">el</span>P</span>
        <span class="title-cross-right">SO</span>
      </h1>

      <p class="front-subtitle">Más 30 relatos<br>de la plaza</p>
      <p class="front-author">Tomás Echeverri</p>
    </section>
  </main>
</body>
</html>
```